Change of trading name, rebrand

existing website to be updated with new theme and logo. existing website is
www.brackenridgeworks.com.au
Industry/Entity Type
Construction
Coding
Coded - Design and coding required
Number of Pages Required
5+ page
Requirements
Must have
- be mobile phone friendly

```html
<!DOCTYPE html>
<html lang="en">
<head>
<meta charset="utf-8">
<meta name="viewport" content="width=1200">
<title>BRW Plant Hire</title>
<link href="https://fonts.googleapis.com/css2?family=Poppins:wght@400;500;600;700&family=Roboto:wght@400;500&family=Arimo:wght@400;700&display=swap" rel="stylesheet">
<style>
:root{
  --navy:#232a80;
  --navy-deep:#0c1059;
  --blue-bright:#0000ee;
  --text:#333;
  --muted:#666;
  --grey-bg:#f4f4f4;
  --gold:#f2c21b;
  --red:#e8101d;
  --touch-bg:#e7efef;
}
*{box-sizing:border-box;margin:0;padding:0}
html,body{width:1200px;height:4277px;overflow:hidden}
body{font-family:'Poppins',sans-serif;color:var(--text);background:#fff;position:relative}
section,header,footer{position:absolute;left:0;width:1200px}
.btn{position:absolute;background:var(--navy);color:#fff;font-weight:600;display:flex;align-items:center;justify-content:center;font-size:17px}
.section-title{position:absolute;left:0;width:100%;text-align:center;font-family:'Roboto',sans-serif;font-weight:400;font-size:33px;color:#333}

/* header */
.site-header{top:0;height:108px;background:#fff;z-index:5}
.brand-badge{position:absolute;left:75px;top:-50px;width:225px;height:228px;border-radius:50%;background:#fff;display:flex;align-items:center;justify-content:center;padding-top:50px}
.brand-name{font-family:'Poppins',sans-serif;font-weight:700;font-size:30px;color:var(--navy);letter-spacing:2px;text-align:center;line-height:1.1}
.brand-name small{display:block;font-size:13px;letter-spacing:4px}
.main-nav{position:absolute;right:24px;top:58px;display:flex;gap:34px;font-size:12.5px;color:var(--navy)}
.main-nav a{color:#4a4f8f;text-decoration:none}
.main-nav a.active{color:var(--navy);font-weight:600}

/* hero */
.hero{top:108px;height:566px;background:linear-gradient(180deg,#d9a56c 0%,#e08b44 30%,#8a5a33 60%,#3f2a1c 100%)}
.hero-panel{position:absolute;left:601px;top:105px;width:536px;height:393px;background:rgba(255,255,255,.62)}
.hero-panel h1{position:absolute;right:36px;top:55px;text-align:right;font-family:'Arimo',sans-serif;font-weight:400;font-size:42px;color:#111;line-height:1.35}
.hero-panel h1 b{font-weight:700;font-size:36px}
.hero-panel p{position:absolute;left:60px;top:180px;width:445px;text-align:center;font-size:13.5px;color:#333;line-height:1.6}
.hero-panel .btn{left:158px;top:274px;width:218px;height:52px}

/* about */
.about{top:674px;height:599px;background:#fff}
.about h2{position:absolute;left:70px;top:148px;font-family:'Roboto',sans-serif;font-weight:400;font-size:32px;color:#333}
.about p{position:absolute;left:70px;top:204px;width:490px;font-size:14.5px;line-height:2.2;color:#555}
.about .btn{left:70px;top:452px;width:164px;height:42px}
.about-ring{position:absolute;left:645px;top:97px;width:416px;height:416px;border-radius:50%;border:3px solid var(--gold);padding:12px}
.about-photo{width:100%;height:100%;border-radius:50%;background:linear-gradient(180deg,#a9cbe6 0%,#cfdbe2 45%,#8d7a5c 75%,#6b5a44 100%)}

/* services */
.services{top:1273px;height:694px;background:var(--grey-bg)}
.services .section-title{top:74px}
.service-card{position:absolute;top:155px;width:311px;height:368px;background:#fff;border:1px solid #ccc}
.service-card.featured{border:2px solid #b6bad8}
.service-photo{height:175px}
.service-card h3{position:absolute;left:14px;top:200px;font-size:15px;font-weight:600;color:#111}
.service-card p{position:absolute;left:14px;top:232px;width:282px;font-size:12px;line-height:1.65;color:#555;height:80px;overflow:hidden}
.service-card .more{position:absolute;right:44px;top:332px;font-size:13px;font-weight:600;color:var(--navy)}
.services .btn{left:501px;top:573px;width:193px;height:56px}

/* gallery */
.gallery{top:1967px;height:445px;background:#fff}
.gallery .section-title{top:76px}
.gallery-item{position:absolute;top:146px;width:181px;height:168px;border:3px solid var(--navy)}
.dots{position:absolute;left:570px;top:352px;display:flex;gap:12px}
.dots span{width:11px;height:11px;border-radius:50%;background:#9aa0c8}
.dots span.on{background:var(--navy)}

/* policies */
.policies{top:2412px;height:596px;background:var(--grey-bg)}
.policies .section-title{top:62px}
.policies .lead{position:absolute;width:100%;top:130px;text-align:center;font-size:20px;font-weight:500;color:var(--navy)}
.policy-btn{position:absolute;width:367px;height:145px;background:var(--navy);color:#fff;font-weight:600;font-size:19px;line-height:1.3;text-align:center;display:flex;align-items:center;justify-content:center;box-shadow:0 0 0 2px #d6d6d6}
.policy-btn.active{background:var(--blue-bright);box-shadow:0 0 0 4px #d0d0d0}

/* cta */
.cta{top:3008px;height:287px;background:linear-gradient(90deg,#3b3531 0%,#4f4944 50%,#3a332e 100%)}
.cta h2{position:absolute;width:100%;top:55px;text-align:center;color:#fff;font-size:34px;font-weight:600;line-height:1.2}
.cta .btn{left:511px;top:172px;width:176px;height:50px;font-size:16px}

/* contact */
.touch{top:3295px;height:584px;background:linear-gradient(120deg,var(--touch-bg),#f3f6f6)}
.touch .section-title{top:60px}
.field{position:absolute;left:201px;width:383px;height:59px;background:#fff;font-size:12px;color:#999;padding:22px 14px}
.field.message{height:100px}
.touch .submit{position:absolute;left:201px;top:491px;width:126px;height:50px;border-radius:14px;background:var(--navy);color:#fff;font-weight:600;font-size:16px;display:flex;align-items:center;justify-content:center}
.touch-photo{position:absolute;left:619px;top:149px;width:364px;height:324px;background:linear-gradient(135deg,#a0553e 0%,#c9866a 45%,#e8e2dc 75%,#cfcac4 100%);border:2px solid #fff}

/* footer */
.site-footer{top:3879px;height:337px;background:var(--navy-deep);color:#fff}
.footer-badge{position:absolute;left:174px;top:95px;width:201px;height:151px;background:#fff;border-radius:10px;display:flex;align-items:center;justify-content:center}
.footer-col{position:absolute;top:100px}
.footer-col h4{font-size:16px;font-weight:600;margin-bottom:22px}
.footer-col ul{list-style:none;font-size:12.5px;line-height:2}
.addr{font-size:12.5px;line-height:1.9;display:flex;gap:10px}
.addr svg{flex:none;margin-top:6px}
.news-input{width:198px;height:34px;background:#fff;color:#777;font-size:12px;padding:9px 8px}
.subscribe{margin-top:12px;width:134px;height:32px;background:var(--red);font-weight:700;font-size:15px;display:flex;align-items:center;justify-content:center}
.copyright{position:absolute;top:4216px;left:0;width:1200px;height:61px;background:#fff;text-align:center;font-size:15px;font-weight:500;color:#111;line-height:61px}
</style>
</head>
<body>

<header class="site-header">
  <div class="brand-badge"><div class="brand-name">BRW<small>PLANT HIRE</small></div></div>
  <nav class="main-nav">
    <a class="active" href="#">Home</a><a href="#">About Us</a><a href="#">Plant Hire</a><a href="#">Project Snapshot</a><a href="#">Policies</a><a href="#">Contact Us</a>
  </nav>
</header>

<section class="hero" role="img" aria-label="Bulldozer on a dirt site at sunset">
  <div class="hero-panel">
    <h1>Committed to superior<br><b>quality plant hire services</b></h1>
    <p>Brackenridge Heavy Equipment Hire specialise in the hire of heavy earthmoving, mining and construction machines with specialised attachments and tooling.</p>
    <div class="btn">Registration Now</div>
  </div>
</section>

<section class="about">
  <h2>About Us</h2>
  <p>We employ a group of highly skilled and capable managers who have worked throughout construction sites in &nbsp;Queensland, NSW and other parts of Australia to deliver a vast array of plant and equipment to mining, civil, building and industrial projects. Our expertise is applied to every project to ensure delivery is achieved in accordance with project specifications, productivity and cost targets.</p>
  <div class="btn">Read More</div>
  <div class="about-ring"><div class="about-photo" role="img" aria-label="Wheel loader lifting its bucket on a site"></div></div>
</section>

<section class="services">
  <h2 class="section-title">Our Services</h2>
  <article class="service-card" style="left:111px">
    <div class="service-photo" role="img" aria-label="Tracked dozer on red earth" style="background:linear-gradient(180deg,#7a4a35,#b08a5a 60%,#6b4a33)"></div>
    <h3>GRADERS FOR HIRE &rsaquo;</h3>
    <p>We own and operate a fleet of Harlan graders for hire, a number of Kovan graders for hire, and a number of larger Terrapin graders in small and large tonnage classes. All</p>
    <span class="more">Read More &rsaquo;</span>
  </article>
  <article class="service-card featured" style="left:445px">
    <div class="service-photo" role="img" aria-label="Truck and wheel loader under blue sky" style="background:linear-gradient(180deg,#7fb1e0,#c9dbe9 50%,#9a8f7d)"></div>
    <h3>LOADERS FOR HIRE &rsaquo;</h3>
    <p>We have a comprehensive range of wheel loaders for hire, and integrated tool carriers available on wet and dry hire contracts for short and long contract terms. We prefer</p>
    <span class="more">Read More &rsaquo;</span>
  </article>
  <article class="service-card" style="left:780px">
    <div class="service-photo" role="img" aria-label="Backhoe loader beside a gravel pile" style="background:linear-gradient(180deg,#f4f4f4,#e9e3da 55%,#c99e6e)"></div>
    <h3>BACKHOE FOR HIRE &rsaquo;</h3>
    <p>Our backhoe hire fleet includes popular brands such as Dalcor, Terra and Nordal backhoes. Our Dalcor backhoe rental range includes a 4 x 4 utility unit with roll over</p>
    <span class="more">Read More &rsaquo;</span>
  </article>
  <div class="btn">View Al Services</div>
</section>

<section class="gallery">
  <h2 class="section-title">Our Gallery</h2>
  <div class="gallery-item" style="left:121px;background:linear-gradient(180deg,#2f6fc7,#8fb1d8 55%,#b08a4a)" role="img" aria-label="Conveyor and loader at a quarry"></div>
  <div class="gallery-item" style="left:315px;background:linear-gradient(180deg,#8f8a84,#d06a3a 50%,#c9c3b8)" role="img" aria-label="Orange excavator on rubble"></div>
  <div class="gallery-item" style="left:509px;background:linear-gradient(180deg,#9aa6b4,#b88a3a 55%,#7c6a55)" role="img" aria-label="Backhoe loading a truck"></div>
  <div class="gallery-item" style="left:703px;background:linear-gradient(180deg,#6d97c9,#c5b88f 55%,#8c7a56)" role="img" aria-label="Yellow dozer on a site"></div>
  <div class="gallery-item" style="left:897px;background:linear-gradient(180deg,#8aa3b8,#d8b43a 50%,#6e6243)" role="img" aria-label="Yellow grader parked outdoors"></div>
  <div class="dots"><span></span><span class="on"></span><span></span></div>
</section>

<section class="policies">
  <h2 class="section-title">World Class Working Policies</h2>
  <p class="lead">Please click on the buttons below to view our policies.</p>
  <div class="policy-btn active" style="left:217px;top:207px">BRW<br>HEALTH &amp; SAFETY<br>POLICY STATEMENT</div>
  <div class="policy-btn" style="left:617px;top:207px">BRW<br>ENVIRONMENTAL<br>POLICY STATEMENT</div>
  <div class="policy-btn" style="left:217px;top:380px">BRW<br>REHABILITATION<br>POLICY STATEMENT</div>
  <div class="policy-btn" style="left:617px;top:380px">BRW<br>COMMERICAL &amp; CREDIT<br>POLICY STATEMENT</div>
</section>

<section class="cta" role="img" aria-label="Dimmed excavator in the background">
  <h2>Contact us today for a<br>FREE QUOTE</h2>
  <div class="btn">Get A Quote</div>
</section>

<section class="touch">
  <h2 class="section-title">Get In Touch</h2>
  <div class="field" style="top:149px">Name</div>
  <div class="field" style="top:224px">Email</div>
  <div class="field" style="top:299px">Phone Number</div>
  <div class="field message" style="top:373px">Message</div>
  <div class="submit">Submit</div>
  <div class="touch-photo" role="img" aria-label="Support agent with a headset working at a laptop"></div>
</section>

<footer class="site-footer">
  <div class="footer-badge"><div class="brand-name">BRW<small>PLANT HIRE</small></div></div>
  <div class="footer-col" style="left:480px">
    <h4>Quick Links</h4>
    <ul><li>Home</li><li>About Us</li><li>Plant Hire</li><li>Project Snapshot</li><li>Policies</li><li>Contact Us</li></ul>
  </div>
  <div class="footer-col" style="left:666px">
    <h4>Address</h4>
    <div class="addr"><svg width="10" height="13" viewBox="0 0 10 13"><path d="M5 0a5 5 0 0 0-5 5c0 4 5 8 5 8s5-4 5-8a5 5 0 0 0-5-5zm0 7a2 2 0 1 1 0-4 2 2 0 0 1 0 4z" fill="#fff"/></svg><span>14 Ridgeline Rd,<br>Coomera QLD 4209</span></div>
    <div class="addr"><svg width="11" height="11" viewBox="0 0 24 24"><path d="M6.6 10.8a15 15 0 0 0 6.6 6.6l2.2-2.2a1 1 0 0 1 1-.25 11 11 0 0 0 3.6.6 1 1 0 0 1 1 1V20a1 1 0 0 1-1 1A17 17 0 0 1 3 4a1 1 0 0 1 1-1h3.5a1 1 0 0 1 1 1 11 11 0 0 0 .6 3.6 1 1 0 0 1-.25 1z" fill="#fff"/></svg><span>1300 000 415<br>07 3000 2718</span></div>
  </div>
  <div class="footer-col" style="left:853px">
    <h4>Newsletter</h4>
    <div class="news-input">Enter Your Email</div>
    <div class="subscribe">SUBSCRIBE</div>
  </div>
</footer>
<div class="copyright">All @Rights By BRW PLANT HIRE.com</div>

</body>
</html>
```